New Business Card

We need to refresh our business cards. We designed these ourselves and we have no graphic design experience. We would like to find a new business card design that is professional and unique. We are an auto finance company. Feel free to play with the logo, but we would like to keep the eye very present on the card. Our corporate colors are green, grey, and white.
Green - RGB - 168,215,27; HEX - #AADD22
Grey - RGB - 196,196,196; HEX - #C4C4C4
Updates
Need to upload the vector file to finalize the project. The last logo was for a jpeg that didn't stretch well.
Industry/Entity Type
Financial Service
Contact Information for Business Card
Honestly don't know...I need your help!

```html
<!DOCTYPE html>
<html lang="en">
<head>
<meta charset="utf-8">
<title>Brightlane Capital – Business Card</title>
<link rel="stylesheet" href="https://fonts.googleapis.com/css2?family=Open+Sans:wght@400;600;700&display=swap">
<style>
  :root {
    --stage: #5b5b5b;
    --card-dark: #302828;
    --card-dark-back: #3a302e;
    --card-grey: #858079;
    --band-grey: #a8a59c;
    --brand-green: #8fb33a;
    --bright-green: #aadd22;
    --olive: #819a48;
    --light-grey: #c4c4c4;
    --white: #ffffff;
  }
  * { box-sizing: border-box; margin: 0; padding: 0; }
  html, body {
    width: 1200px; height: 1200px; overflow: hidden;
    background: var(--stage);
    font-family: "Open Sans", Arial, sans-serif;
  }
  .canvas { position: relative; width: 1200px; height: 1200px; }

  .card {
    position: absolute; left: 240px; width: 720px; height: 420px;
    border-radius: 29px; overflow: hidden;
  }

  /* Front */
  .card--front { top: 142px; background: var(--card-dark); }
  .front-brand {
    position: absolute; top: 150px; left: 0; right: 0;
    display: flex; justify-content: center; align-items: center; gap: 18px;
  }
  .brand-dot { width: 54px; height: 54px; border-radius: 50%; background: var(--light-grey); }
  .brand-name {
    color: var(--brand-green); font-weight: 600; font-size: 46px; letter-spacing: 0.5px;
  }
  .front-web {
    position: absolute; top: 346px; left: 0; right: 0; text-align: center;
    color: var(--light-grey); font-size: 22px;
  }
  .front-accent {
    position: absolute; top: 384px; left: 102px; width: 540px; height: 14px;
    background: var(--brand-green); border-radius: 8px 8px 0 0;
  }
  .front-band {
    position: absolute; bottom: 0; left: 0; right: 0; height: 26px; background: var(--band-grey);
  }

  /* Back */
  .card--back { top: 638px; }
  .back-shapes { position: absolute; inset: 0; width: 720px; height: 420px; }
  .name-tab {
    position: absolute; left: 0; top: 36px; width: 6px; height: 46px;
    background: var(--white); border-radius: 0 4px 4px 0;
  }
  .person { position: absolute; left: 25px; top: 40px; color: var(--white); }
  .person-name { font-size: 28px; font-weight: 700; line-height: 1.1; }
  .person-title { font-size: 15.5px; font-weight: 700; color: #e6e4df; margin-top: 4px; }

  .contact-list { position: absolute; left: 22px; top: 152px; list-style: none; }
  .contact-item {
    display: flex; align-items: center; gap: 10px; height: 32px;
    color: var(--white); font-size: 23px;
  }
  .contact-item + .contact-item { margin-top: 18px; }
  .contact-item:nth-child(3) { margin-top: 23px; }
  .contact-item:nth-child(4) { margin-top: 30px; }
  .contact-icon { width: 24px; height: 24px; flex: none; }

  .back-brand {
    position: absolute; left: 440px; top: 212px;
    display: flex; align-items: center; gap: 12px;
  }
  .back-brand .brand-dot { width: 40px; height: 40px; }
  .back-brand .brand-name { font-size: 30px; }
</style>
</head>
<body>
<div class="canvas">

  <section class="card card--front">
    <div class="front-brand">
      <span class="brand-dot"></span>
      <span class="brand-name">Brightlane Capital</span>
    </div>
    <p class="front-web">www.brightlanecapital.com</p>
    <div class="front-accent"></div>
    <div class="front-band"></div>
  </section>

  <section class="card card--back">
    <svg class="back-shapes" viewBox="0 0 600 350" preserveAspectRatio="none">
      <rect width="600" height="350" fill="var(--card-dark-back)"/>
      <path d="M240 0 L482 0 C405 45 350 120 336 232 L300 250 Z" fill="var(--bright-green)"/>
      <path d="M240 0 L406 0 C362 45 338 120 332 212 L300 250 Z" fill="var(--olive)"/>
      <path d="M0 0 L240 0 C285 80 305 160 338 212 C372 262 400 305 428 350 L0 350 Z" fill="var(--card-grey)"/>
    </svg>

    <div class="name-tab"></div>
    <div class="person">
      <h1 class="person-name">Darren Whitlow</h1>
      <p class="person-title">CEO and Co-founder</p>
    </div>

    <ul class="contact-list">
      <li class="contact-item">
        <svg class="contact-icon" viewBox="0 0 24 24" fill="none" stroke="var(--bright-green)" stroke-width="1.6" stroke-linecap="round" stroke-linejoin="round">
          <path d="M5 3h4l2 5-2.5 1.5a11 11 0 0 0 6 6L16 13l5 2v4a2 2 0 0 1-2 2A16 16 0 0 1 3 5a2 2 0 0 1 2-2z"/>
          <path d="M15 3a6 6 0 0 1 6 6M15 6.5a3 3 0 0 1 2.5 2.5"/>
        </svg>
        <span>+0400 555 019</span>
      </li>
      <li class="contact-item">
        <svg class="contact-icon" viewBox="0 0 24 24">
          <rect x="2" y="5" width="20" height="14" rx="1.5" fill="var(--bright-green)"/>
          <path d="M2.5 6l9.5 7 9.5-7" fill="none" stroke="var(--card-grey)" stroke-width="1.6"/>
        </svg>
        <span>hello@brightlane.com</span>
      </li>
      <li class="contact-item">
        <svg class="contact-icon" viewBox="0 0 24 24" fill="none" stroke="var(--bright-green)" stroke-width="1.5">
          <circle cx="12" cy="12" r="9.5"/>
          <ellipse cx="12" cy="12" rx="4.2" ry="9.5"/>
          <path d="M2.5 12h19M4 7h16M4 17h16"/>
        </svg>
        <span>www.brightlanecapital.com</span>
      </li>
      <li class="contact-item">
        <svg class="contact-icon" viewBox="0 0 24 24" fill="none" stroke="var(--bright-green)" stroke-width="1.6" stroke-linejoin="round">
          <path d="M12 18s-6-6-6-10a6 6 0 0 1 12 0c0 4-6 10-6 10z"/>
          <circle cx="12" cy="8" r="2.2"/>
          <path d="M7 16H3l-1 6h20l-1-6h-4"/>
        </svg>
        <span>48 Elm Ave. Springvale, FL 32010</span>
      </li>
    </ul>

    <div class="back-brand">
      <span class="brand-dot"></span>
      <span class="brand-name">Brightlane Capital</span>
    </div>
  </section>

</div>
</body>
</html>
```